VOIP company busioness card redesign

Redesign business card to match our new logo and marketing material. Should include logo on one side and contact information on other side.

We like modern and clean

Industry/Entity Type

Phone Company

Contact Information for Business Card

One side should be logo other side should include contact info
Name
Phone Number
email
website

Font styles to use
Other font styles liked:
• dont care

Requirements
Must have
• Modern sleek design that works with our logo

```html
<!DOCTYPE html>
<html lang="en">
<head>
<meta charset="utf-8">
<title>Nuvex Solutions — Business Card</title>
<link rel="stylesheet" href="https://fonts.googleapis.com/css2?family=Poppins:wght@400;500;600;700&display=swap">
<style>
  :root {
    --bg: #ededed;
    --card-light: #f7f7f5;
    --card-dark-top: #1b2832;
    --card-dark-bottom: #2b3c47;
    --brand-blue: #1f8fd0;
    --ink: #1d1d1d;
    --muted: #8a8a8a;
    --muted-dark: #9aa3a9;
    --accent-green: #8cc63f;
  }
  * { box-sizing: border-box; margin: 0; padding: 0; }
  html, body {
    width: 1200px; height: 800px; overflow: hidden;
    background: var(--bg);
    font-family: "Poppins", Arial, sans-serif;
  }
  .stage {
    position: relative; width: 1200px; height: 800px;
    display: flex; align-items: center; justify-content: center; gap: 60px;
  }
  .card {
    position: relative; width: 520px; height: 300px;
    border-radius: 22px;
    box-shadow: 0 10px 30px rgba(0,0,0,.12);
    overflow: hidden;
  }
  .card--front { background: var(--card-light); }
  .card--back {
    background: linear-gradient(160deg, var(--card-dark-top), var(--card-dark-bottom));
    display: flex; align-items: center; justify-content: center;
  }
  .brand { display: flex; flex-direction: column; }
  .brand__row { display: flex; align-items: center; gap: 10px; }
  .brand__mark {
    width: 14px; height: 14px; border-radius: 50%;
    background: var(--accent-green);
  }
  .brand__name {
    font-weight: 700; color: var(--brand-blue); letter-spacing: -0.5px; line-height: 1;
  }
  .brand__tagline { color: var(--muted); font-weight: 400; }

  .card--front .brand { position: absolute; left: 44px; top: 44px; }
  .card--front .brand__name { font-size: 44px; }
  .card--front .brand__tagline { font-size: 10px; margin-top: 8px; }

  .card--back .brand { align-items: flex-start; }
  .card--back .brand__name { font-size: 64px; }
  .card--back .brand__mark { width: 18px; height: 18px; }
  .card--back .brand__tagline { font-size: 13px; margin-top: 10px; color: var(--muted-dark); }

  .contact { position: absolute; left: 250px; top: 128px; }
  .contact__name { font-size: 26px; font-weight: 500; color: var(--ink); line-height: 1.1; }
  .contact__title { font-size: 15px; color: var(--brand-blue); margin-top: 2px; margin-bottom: 10px; }
  .contact__list { list-style: none; }
  .contact__item {
    display: flex; align-items: center; gap: 10px;
    font-size: 15px; color: var(--ink); line-height: 1.7;
  }
  .contact__icon { width: 14px; height: 14px; flex: none; }
</style>
</head>
<body>
<main class="stage">
  <section class="card card--front" aria-label="Business card, contact side">
    <div class="brand">
      <div class="brand__row">
        <span class="brand__name">Nuvex</span>
        <span class="brand__mark"></span>
      </div>
      <span class="brand__tagline">Voice Networks Made Simple Today</span>
    </div>

    <div class="contact">
      <p class="contact__name">Joe Smith</p>
      <p class="contact__title">Job Title</p>
      <ul class="contact__list">
        <li class="contact__item">
          <svg class="contact__icon" viewBox="0 0 16 16" aria-hidden="true">
            <path fill="#1f8fd0" d="M3.6 1.5l2.3 2.6-1.3 1.7a9 9 0 0 0 5.6 5.6l1.7-1.3 2.6 2.3-1.4 2.1C7.6 14.5 1.5 8.4 1.5 2.9z"/>
          </svg>
          <span>000 000 0000</span>
        </li>
        <li class="contact__item">
          <svg class="contact__icon" viewBox="0 0 16 16" aria-hidden="true">
            <rect x="1" y="3" width="14" height="10" rx="1.5" fill="#1f8fd0"/>
            <path d="M1.5 4l6.5 5 6.5-5" fill="none" stroke="#fff" stroke-width="1.2"/>
          </svg>
          <span>Email@xyz.com</span>
        </li>
        <li class="contact__item">
          <svg class="contact__icon" viewBox="0 0 16 16" aria-hidden="true">
            <g fill="none" stroke="#1f8fd0" stroke-width="1.3">
              <circle cx="8" cy="8" r="6.5"/>
              <ellipse cx="8" cy="8" rx="2.8" ry="6.5"/>
              <path d="M1.5 8h13M2.6 4.6h10.8M2.6 11.4h10.8"/>
            </g>
          </svg>
          <span>www.yourwebsite.com</span>
        </li>
      </ul>
    </div>
  </section>

  <section class="card card--back" aria-label="Business card, logo side">
    <div class="brand">
      <div class="brand__row">
        <span class="brand__name">Nuvex</span>
        <span class="brand__mark"></span>
      </div>
      <span class="brand__tagline">Voice Networks Made Simple Today</span>
    </div>
  </section>
</main>
</body>
</html>
```